Web Developer Needs a Business Card Design

I need a personal business card design that represents me as a web developer for potential employers. I would like the background to be a dark color on the front for contrast with my logo and name. The back will have all my information along with a smaller version of the logo. I want something with a modern look and feel, not too conservative. This will be used for potential employers and freelance work.

Industry/Entity Type

Business

Contact Information for Business Card

Front should have my logo and name. The back should have all my personal information which would include: name: Tom Brevardi, phone: 570-614-9083, email: tombrevardi@mailwisp.com, website url: www.tombrevardi.com, logo, web developer.

Font styles to use
Sans Serif

Requirements
Must have
• Must include my logo. The color palette base color will be the logo color.

```html
<!DOCTYPE html>
<html lang="en">
<head>
<meta charset="utf-8">
<title>Tom Brevardi — Business Card</title>
<link rel="stylesheet" href="https://fonts.googleapis.com/css2?family=Federo&family=Arimo:wght@400&display=swap">
<style>
  :root {
    --accent: #5ae6c9;
    --bg-light: #2b2b2b;
    --bg-mid: #1a1a1a;
    --bg-dark: #0b0b0b;
  }
  html, body {
    margin: 0;
    padding: 0;
    overflow: hidden;
    background: var(--bg-dark);
  }
  .card {
    position: relative;
    width: 1200px;
    height: 683px;
    overflow: hidden;
  }
  .card-texture {
    position: absolute;
    inset: 0;
    background: linear-gradient(115deg, var(--bg-light) 0%, var(--bg-mid) 45%, var(--bg-dark) 100%);
  }
  .brand-ring {
    position: absolute;
    left: 0;
    top: 0;
  }
  .brand-name {
    position: absolute;
    left: 60px;
    top: 230px;
    width: 460px;
    text-align: center;
    font-family: "Federo", sans-serif;
    font-size: 58px;
    line-height: 1;
    color: var(--accent);
  }
  .owner {
    position: absolute;
    right: 50px;
    top: 478px;
    width: 580px;
    text-align: right;
  }
  .owner-name {
    margin: 0;
    font-family: "Federo", sans-serif;
    font-weight: 400;
    font-size: 80px;
    line-height: 1;
    color: var(--accent);
    padding-bottom: 8px;
    border-bottom: 4px solid var(--accent);
    text-align: center;
  }
  .owner-site {
    margin: 14px 6px 0 0;
    font-family: "Arimo", sans-serif;
    font-size: 31px;
    color: var(--accent);
  }
</style>
</head>
<body>
  <main class="card">
    <div class="card-texture" role="img" aria-label="Dark carbon fibre texture background"></div>

    <svg class="brand-ring" width="1200" height="683" viewBox="0 0 1200 683" aria-hidden="true">
      <circle cx="292" cy="262" r="302" fill="none" stroke="var(--accent)" stroke-width="22"/>
    </svg>
    <div class="brand-name">Tom Brevardi</div>

    <section class="owner">
      <h1 class="owner-name">Tom Brevardi</h1>
      <p class="owner-site">www.tombrevardi.com</p>
    </section>
  </main>
</body>
</html>
```